Visitenkarten-Design für Steuerberater und Wirtschaftsprüfer
Zielgruppe
Steuerberater, Wirtschaftsprüfer in München
Aufgabenstellung
Wir haben ein Logo das uns gefällt, jetzt allerdings steht die Umfirmierung vor der Tür und aus der Kanzlei Wendeholt (so unser Name) wird Wendeholt und Partner mbB (die Jugend kommt mit als Partner in die Kanzlei) , Steuerberater, Wirtschaftsprüfer
Analog unseres alten Briefpapiers und der alten Visitenkarten soll eigentlich nur der Zusatz 'und Partner mbB' oder '& Partner mbB' gestaltet werden.
Das Dateiformat bei Visitenkarten bitte so übergeben, dass wir Namen selbst austauschen mit gängigen Officeprogrammen austauschen können. Bei den Visitenkarten ist das große 'Wendeholt' geprägt.
Ich stelle das Logo, das aktuelle Briefpapier und aktuelle Visitenkarten ein. Unsere Farbe ist grau.
Das Logo bitte in .pdf, .png, .psd und .eps (sagt mi alles nichts, haben wir aber alles schon mal irgendwo gebraucht) , Visiten karten auch in .pddf und .ai
Bei Fragen kontaktiert mich gern jederzeit.

```html
<!DOCTYPE html>
<html lang="de">
<head>
<meta charset="utf-8">
<title>Briefbogen Wendeholt &amp; Partner mbB</title>
<link href="https://fonts.googleapis.com/css2?family=Arimo:wght@400;700&family=Tinos&display=swap" rel="stylesheet">
<style>
  :root {
    --backdrop: #1e1e1e;
    --paper: #ffffff;
    --band: #d2d2d3;
    --ink: #1a1a1a;
    --brand-grey: #58585a;
    --meta-grey: #8a8a8a;
    --guide-red: #d0202a;
  }
  * { margin: 0; padding: 0; box-sizing: border-box; }
  html, body { width: 1101px; height: 1200px; overflow: hidden; background: var(--backdrop); }
  body { position: relative; font-family: "Arimo", Arial, sans-serif; color: var(--ink); }

  .sheet { position: absolute; left: 144px; top: 15px; width: 817px; height: 1145px; background: var(--paper); }
  .band { position: absolute; background: var(--band); }
  .band--top-left { left: 0; top: 47px; width: 277px; height: 52px; }
  .band--top-right { left: 532px; top: 47px; width: 285px; height: 52px; }
  .band--foot-left { left: 0; top: 1100px; width: 97px; height: 45px; }
  .band--foot-right { left: 720px; top: 1100px; width: 97px; height: 45px; }

  .brand { position: absolute; left: 277px; top: 35px; width: 255px; text-align: center; color: var(--brand-grey); }
  .brand__name { font-weight: 700; font-size: 25px; line-height: 29px; letter-spacing: 1px; text-transform: uppercase; }
  .brand__name-line { display: block; }
  .brand__tagline { font-size: 10px; letter-spacing: 0.4px; line-height: 12px; margin-top: 2px; }

  .sender-line { position: absolute; left: 97px; top: 194px; font-size: 6.5px; color: var(--meta-grey); white-space: nowrap; }
  .sender-line b { color: #555; }

  .recipient { position: absolute; left: 97px; top: 211px; font-size: 15px; line-height: 19.3px; }
  .date { position: absolute; right: 98px; top: 351px; font-size: 15px; }
  .subject { position: absolute; left: 97px; top: 386px; font-size: 18px; font-weight: 700; }

  .body-text { position: absolute; left: 97px; top: 445px; font-size: 15px; line-height: 19.2px; white-space: nowrap; }
  .body-text p { margin-bottom: 19px; }
  .closing { position: absolute; left: 97px; top: 792px; font-size: 15px; }
  .signature { position: absolute; left: 97px; top: 869px; font-size: 15px; line-height: 19.3px; }

  .fold-mark { position: absolute; left: 20px; width: 3px; height: 3px; border-radius: 50%; background: #999; }

  .footer { position: absolute; left: 97px; top: 1098px; width: 623px; text-align: center; font-size: 10.5px; line-height: 15px; color: var(--meta-grey); white-space: nowrap; }
  .footer b { color: #6a6a6a; }

  .guides { position: absolute; left: 0; top: 0; }
  .guide-note { position: absolute; font-family: "Tinos", "Times New Roman", serif; font-size: 16px; line-height: 20px; color: var(--guide-red); white-space: nowrap; }
</style>
</head>
<body>
  <div class="sheet">
    <div class="band band--top-left"></div>
    <div class="band band--top-right"></div>

    <div class="brand">
      <div class="brand__name"><span class="brand__name-line">Wendeholt</span><span class="brand__name-line">&amp; Partner mbB</span></div>
      <div class="brand__tagline">STEUERBERATER | WIRTSCHAFTSPRÜFER</div>
    </div>

    <div class="sender-line"><b>KANZLEI HANNA L. WENDEHOLT</b> | Lindenhofstr. 22 | 80471 München</div>

    <div class="recipient">Musterfirma<br>Max Mustermann<br>Adresszusatz<br>Musterstraße 123<br>12345 Musterstadt<br>Musterland</div>

    <div class="date">München, 00. Monat 2014</div>
    <div class="subject">Betreffzeile</div>

    <span class="fold-mark" style="top:376px"></span>
    <span class="fold-mark" style="top:576px"></span>

    <div class="body-text">
      <p>Sehr geehrter Herr Mustermann,</p>
      <p>Kurzer Brief an ein Idol. Lieber Onkel Konrad, schon lange wollte ich Dir sagen, daß ich<br>Dich für einen ganz tollen Texter halte. Ich weiß, Du hörst sehr gerne Lob, und deshalb kann<br>man nicht oft genug sagen, daß Du der Größte bist.</p>
      <p>Gerade in Deinem Alter ist man ja gesegnet, wenn man noch so witzig schreiben kann wie<br>Du. Viele Deiner Werberkollegen sind ja schon zu wichtig, um noch den Humor zu haben.</p>
      <p>Du bist da ganz anders. Du kannst richtig komisch sein. Und das, obwohl Du in Deinem sehr<br>langen Leben auch schon sehr viele unangenehme Dinge schreiben mußtest. Texte<br>für Burgerhaus zum Beispiel. Oder kleine Reime für Onkel Egon. Nein, Du hast es wirklich<br>nicht leicht gehabt. Und dann noch die Selbstdarstellung für Tante Frieda.</p>
      <p>Gerade in Deinem Alter ist man ja gesegnet, wenn man noch so witzig schreiben kann wie<br>Du. Viele Deiner Werberkollegen sind ja schon zu wichtig, um noch den Humor zu haben.</p>
    </div>

    <div class="closing">Mit freundlichen Grüßen</div>
    <div class="signature">Vorname Name<br>Titel</div>

    <div class="band band--foot-left"></div>
    <div class="band band--foot-right"></div>
    <div class="footer">
      <b>WendeholtPartner mbB</b> | Lindenhofstr. 22 | 80471 München<br>
      <b>fon</b> 089-41207730 | <b>fax</b> 089-41207739 | <b>mail</b> info@kanzlei-wendeholt.de | <b>web</b> www.kanzlei-wendeholt.de<br>
      <b>UstID</b> DE 123456789 | <b>IBAN</b> DE 00 1234 5678 9012 3456 78 | <b>BIC</b> MUSTDEX1XXX
    </div>
  </div>

  <svg class="guides" width="1101" height="1200" viewBox="0 0 1101 1200" aria-hidden="true">
    <g stroke="#d0202a" stroke-width="1" fill="none">
      <line x1="241.5" y1="15" x2="241.5" y2="230"/>
      <line x1="144" y1="229.5" x2="241" y2="229.5"/>
      <line x1="864" y1="229.5" x2="961" y2="229.5"/>
      <line x1="144" y1="692.5" x2="241" y2="692.5"/>
      <line x1="864" y1="692.5" x2="961" y2="692.5"/>
      <line x1="384" y1="284.5" x2="455" y2="284.5"/>
      <line x1="686.5" y1="788" x2="686.5" y2="860"/>
    </g>
    <g fill="#d0202a">
      <polygon points="378,284.5 386,281 386,288"/>
      <polygon points="686.5,781 683,789 690,789"/>
    </g>
  </svg>

  <div class="guide-note" style="left:249px;top:140px">55 mm</div>
  <div class="guide-note" style="left:168px;top:207px">25 mm</div>
  <div class="guide-note" style="left:888px;top:207px">25 mm</div>
  <div class="guide-note" style="left:168px;top:670px">25 mm</div>
  <div class="guide-note" style="left:888px;top:670px">25 mm</div>
  <div class="guide-note" style="left:459px;top:264px">Anschriftenfeld:<br>75mm breit, 30mm hoch<br>Schrift: Arial, 11pt, 6 mögliche<br>Zeilen</div>
  <div class="guide-note" style="left:687px;top:868px">Textfeld:<br>160mm breit,180mm hoch<br>Schrift: Arial, 11pt (Betreff 14pt bold)</div>
</body>
</html>
```